Looking for a full stationery set design for our business - NO generic/stock templates please.

I am looking for a complete stationary set for my used car dealership. I am looking for something, unique, creative, classy and high-end. Generic designs or anything that looks like a 'stock' template will not be selected. Please do not use a vehicle image in the design - - that is too predictable for a car dealership.

I prefer matte designs over shiny/glossy designs but will consider both if the look is right. I have attached a few different variations of our logo you can work with, as well as a QR code to our website.

These are the items needed:
- Letterhead (with MS word file)
- Envelope #10
- Envelope 9" x 12"
- Envelope 10" x 13"
- Presentation Folder 9" x 12"
- Business Cards 2" x 3.5"
- Folded Card (5.5 x 8" folded to 4" x 5.5")
- Notepad Small (4" x 6")
- Notepad Large (5.5" x 8.5")
- Postcard (4" x 6")

Low design entries Many entries from the same designers Many repetitive designs Too many generic entries that look like stock templates

• Original, creative work, high-end/classy appeal. Must stand out as high-quality, professional image that captures your attention.
• No generic/stock templates or anything that looks like it.

```html
<!DOCTYPE html>
<html lang="en">
<head>
<meta charset="utf-8">
<title>Redline Auto Yard – Stationery Set</title>
<link href="https://fonts.googleapis.com/css2?family=Open+Sans:wght@400;600;800&display=swap" rel="stylesheet">
<style>
  :root{
    --backdrop:#8b8c91;
    --navy:#2a2c38;
    --blue:#1b78c3;
    --paper:#f5f5f4;
    --rule:#b9bcc2;
    --muted:#5a5d68;
  }
  *{box-sizing:border-box;margin:0;padding:0}
  html,body{width:1200px;height:792px;overflow:hidden}
  body{background:var(--backdrop);font-family:"Open Sans",Arial,sans-serif;position:relative}
  .piece{position:absolute;overflow:hidden;background:var(--paper)}
  .piece svg.art{position:absolute;left:0;top:0}
  .wordmark{font-weight:800;color:var(--navy);line-height:1;letter-spacing:-0.02em;position:absolute;white-space:nowrap}
  .wordmark.light{color:var(--paper)}
  .contact{position:absolute;color:var(--paper);font-size:6.5px;line-height:1.45;white-space:nowrap}
  .contact .row{display:flex;align-items:center;gap:3px}
  .contact .dot{width:4px;height:4px;border-radius:50%;background:var(--blue);display:inline-block;flex:none}
  .contact .label{color:var(--blue);font-weight:600}
  .divider{position:absolute;width:1px;background:var(--muted)}

  /* business card back */
  .card-back{left:98px;top:91px;width:204px;height:118px;background:var(--navy)}
  .card-back .wordmark{left:0;right:0;top:47px;text-align:center;font-size:19px}

  /* business card front */
  .card-front{left:98px;top:258px;width:204px;height:116px}
  .card-front .wordmark{right:8px;top:15px;font-size:12px}
  .card-front .person{position:absolute;left:8px;top:36px}
  .card-front .person-name{color:var(--blue);font-weight:600;font-size:8px}
  .card-front .person-role{color:var(--navy);font-size:5.5px}
  .card-front .contact{font-size:5.6px}
  .card-front .contact .dot{width:3.5px;height:3.5px}
  .card-front .contact.phone{left:8px;top:84px}
  .card-front .divider{left:82px;top:86px;height:22px}
  .card-front .contact.address{left:88px;top:84px}

  /* notepad */
  .notepad{left:106px;top:408px;width:194px;height:294px}
  .notepad .wordmark{left:0;right:0;top:22px;text-align:center;font-size:15px}
  .notepad .lines{position:absolute;left:10px;right:10px;top:64px}
  .notepad .lines span{display:block;height:11.7px;border-bottom:1px solid var(--rule)}
  .notepad .foot{position:absolute;bottom:10px;left:5px;right:5px;height:5px;display:flex;gap:4px}
  .notepad .foot .blue{flex:1;background:var(--blue)}
  .notepad .foot .dark{flex:1;background:var(--navy)}

  /* letterhead */
  .letterhead{left:372px;top:104px;width:294px;height:416px}
  .letterhead .wordmark{left:13px;top:20px;font-size:14px}
  .letterhead .contact.phone{left:14px;top:380px}
  .letterhead .divider{left:104px;top:382px;height:26px}
  .letterhead .contact.address{left:112px;top:380px}

  /* folder */
  .folder{left:720px;top:84px;width:330px;height:438px;background:var(--navy)}
  .folder .wordmark{left:0;right:0;top:98px;text-align:center;font-size:40px;line-height:1.05}

  /* envelope #10 */
  .envelope{left:366px;top:552px;width:296px;height:162px}
  .envelope .flap{position:absolute;left:0;top:0;width:296px;height:40px;background:var(--navy);clip-path:polygon(0 0,100% 0,96% 70%,90% 100%,10% 100%,4% 70%)}
  .envelope .wordmark{left:0;right:0;top:12px;text-align:center;font-size:12px}

  /* postcard */
  .postcard{left:756px;top:552px;width:328px;height:163px}
  .postcard .wordmark{right:12px;top:18px;font-size:15px}
</style>
</head>
<body>

  <section class="piece card-back" aria-label="Business card, back">
    <div class="wordmark light">Redline Auto Yard</div>
  </section>

  <section class="piece card-front" aria-label="Business card, front">
    <svg class="art" width="204" height="116" viewBox="0 0 204 116">
      <path d="M0 116 L0 74 C45 60 105 56 145 66 C170 74 185 92 193 116 Z" fill="var(--navy)"/>
      <path d="M120 58 C160 56 195 78 204 98 L204 108 C190 84 160 66 128 62 Z" fill="var(--blue)"/>
    </svg>
    <div class="wordmark">Redline Auto Yard</div>
    <div class="person">
      <div class="person-name">Daniel R. Hale</div>
      <div class="person-role">Founder &amp; CEO</div>
    </div>
    <div class="contact phone">
      <div class="row"><i class="dot"></i>000 000 0000</div>
      <div class="row"><i class="dot"></i>RedlineAuto.com</div>
      <div class="row"><i class="dot"></i>dan@RedlineAuto.com</div>
    </div>
    <div class="divider"></div>
    <div class="contact address">
      <div class="label">Address:</div>
      <div>418 Cedar Avenue</div>
      <div>Brookfield&nbsp; MI 48019</div>
    </div>
  </section>

  <section class="piece notepad" aria-label="Notepad">
    <div class="wordmark">Redline Auto Yard</div>
    <div class="lines">
      <span></span><span></span><span></span><span></span><span></span><span></span>
      <span></span><span></span><span></span><span></span><span></span><span></span>
      <span></span><span></span><span></span><span></span><span></span><span></span>
    </div>
    <div class="foot"><i class="blue"></i><i class="dark"></i></div>
  </section>

  <section class="piece letterhead" aria-label="Letterhead">
    <svg class="art" width="294" height="416" viewBox="0 0 294 416">
      <path d="M0 416 L0 372 C60 344 160 336 222 356 C250 368 262 392 268 416 Z" fill="var(--navy)"/>
      <path d="M150 340 C215 338 270 360 294 392 L294 406 C272 376 230 352 172 346 Z" fill="var(--blue)"/>
    </svg>
    <div class="wordmark">Redline Auto Yard</div>
    <div class="contact phone">
      <div class="row"><i class="dot"></i>000 000 0000</div>
      <div class="row"><i class="dot"></i>RedlineAuto.com</div>
      <div class="row"><i class="dot"></i>dan@RedlineAuto.com</div>
    </div>
    <div class="divider"></div>
    <div class="contact address">
      <div class="label">Address:</div>
      <div>418 Cedar Avenue</div>
      <div>Brookfield&nbsp; MI 48019</div>
    </div>
  </section>

  <section class="piece folder" aria-label="Presentation folder">
    <svg class="art" width="330" height="438" viewBox="0 0 330 438">
      <path d="M0 438 L0 366 C70 338 190 332 262 352 C300 364 322 390 330 410 L330 438 Z" fill="var(--blue)"/>
      <path d="M196 340 C250 344 292 368 312 400 L306 402 C286 372 246 350 196 344 Z" fill="var(--navy)"/>
    </svg>
    <div class="wordmark light">Redline<br>Auto Yard</div>
  </section>

  <section class="piece envelope" aria-label="Envelope #10">
    <div class="flap"></div>
    <div class="wordmark light">Redline Auto Yard</div>
  </section>

  <section class="piece postcard" aria-label="Postcard">
    <svg class="art" width="328" height="163" viewBox="0 0 328 163">
      <path d="M0 163 L0 100 C70 78 170 70 232 84 C265 94 285 128 292 163 Z" fill="var(--navy)"/>
      <path d="M150 74 C220 70 292 96 328 134 L328 146 C296 108 236 82 170 78 Z" fill="var(--blue)"/>
    </svg>
    <div class="wordmark">Redline Auto Yard</div>
  </section>

</body>
</html>
```